Example of School Sign for Digital Siganage

We sell digital signage software and screens. I have an expo coming up and I want some examples of typical images and messages that a school might use on an outdoor screen for public viewing. The resolution of the screen is quite low at 504 pixels wide by 336 pixels high. This means that we cannot use anything too small or detailed. The images could however be created at 1008 x 672 and that way they will scale down. The images need to be delivered in .psd format with all layers available.

We will call the School Stonemere Heights College. We want the school name on all the images (slides) and a fictitious logo associated with the name. Examples of the images required would be. . .

1. Congratulations to Lucy Pembridge School Dux 2015. (This would have an image of a smiling teenage girl.)

2. Team of the Week. Year 10 Girls under 16 Soccer Team. 5-Wins 0-Losses. (This would have a picture of girls playing soccer.)

3. School Production of Brassline. August 12th -17th. Get your tickets from the office . (An image of a Brassline logo)

4. Car Wash at School the Sunday to raise funds for the Year 9 Singapore Trip. (Image of students washing a car)

5. School Holidays Start Friday the 8th of September. School re-opens Monday 25th of September. (An image of a crowd of happy students)

6. Student of the Week. Tobin Walsh, Winner of the Meridian Automaton Shield. (image of teenage student with robot)

Hopefully this is clear.

Industry/Entity Type

Digital Signage

Font styles to use
Sans Serif

Requirements
Must have
• School Name and Logo
Should not have
• Any very small fonts or too much fine detail

```html
<!DOCTYPE html>
<html lang="en">
<head>
<meta charset="utf-8">
<title>Stonemere Heights College – Signage Slides</title>
<link rel="stylesheet" href="https://fonts.googleapis.com/css2?family=Source+Sans+3:wght@600;700&family=Open+Sans:wght@400&family=Signika:wght@700&display=swap">
<style>
:root{
  --navy:#163a6b;
  --blue:#15558f;
  --red:#b5121b;
  --ink:#231f20;
  --white:#ffffff;
  --rule:#9a9a9a;
  --sky:#a9d3ee;
  --grass:#6f9a3c;
}
*{margin:0;padding:0;box-sizing:border-box}
html,body{width:873px;height:1200px;overflow:hidden;background:var(--white)}
.canvas{position:relative;width:873px;height:1200px;overflow:hidden}
.stage{position:absolute;left:0;top:0;width:1008px;height:1386px;transform:scale(0.8661);transform-origin:0 0}
.slide{position:absolute;left:0;width:1008px;height:640px;overflow:hidden;background:var(--white)}
.slide--carwash{top:0;height:672px;border-bottom:1px solid var(--rule)}
.slide--holidays{top:746px;border-top:1px solid var(--rule)}
.slide svg.shapes{position:absolute;left:0;top:0}
.school-name{position:absolute;left:640px;width:312px;text-align:center;font-family:"Open Sans",sans-serif;font-weight:400;color:var(--ink);line-height:1.15}
.school-name__mark{display:block;width:34px;height:34px;border-radius:50%;background:var(--red);margin:0 auto 14px}
.school-name__text{font-size:33px;letter-spacing:.5px}
.slide--carwash .school-name{top:40px}
.slide--holidays .school-name{top:34px}
.event-tag{position:absolute;left:0;top:35px;width:468px;height:96px;background:var(--red);color:var(--white);font-family:"Source Sans 3",sans-serif;font-weight:700;font-size:70px;line-height:96px;padding-left:46px;letter-spacing:-1px;text-shadow:3px 3px 0 #3a0a0c}
.event-date{position:absolute;left:580px;width:400px;top:290px;text-align:center;font-family:"Source Sans 3",sans-serif;font-weight:700;font-size:52px;color:var(--red)}
.event-cause{position:absolute;left:620px;width:340px;top:402px;text-align:center;font-family:"Signika",sans-serif;font-weight:700;color:var(--navy);font-size:33px;line-height:1.4}
.holiday-copy{position:absolute;left:0;width:1008px;text-align:center;color:var(--white);font-family:"Source Sans 3",sans-serif;font-weight:700}
.holiday-copy--title{top:352px;font-size:66px;line-height:86px;left:-5px}
.holiday-copy--sub{top:556px;font-size:35px}
sup{font-size:.55em;vertical-align:super;line-height:0}
</style>
</head>
<body>
<div class="canvas">
<div class="stage">

  <section class="slide slide--carwash">
    <svg class="shapes" width="1008" height="672" viewBox="0 0 1008 672">
      <defs>
        <linearGradient id="carwashScene" x1="0" y1="0" x2="0" y2="1">
          <stop offset="0" stop-color="var(--sky)"/>
          <stop offset=".35" stop-color="#d9d2c4"/>
          <stop offset=".55" stop-color="#c9c9c9"/>
          <stop offset=".7" stop-color="var(--grass)"/>
          <stop offset="1" stop-color="#4f7a2a"/>
        </linearGradient>
      </defs>
      <polygon points="0,0 605,0 405,240 625,672 0,672" fill="url(#carwashScene)" role="img" aria-label="Photo of two smiling students holding hand-painted car wash signs in a school car park"/>
      <polygon points="605,0 660,0 455,240 670,672 625,672 405,240" fill="var(--blue)"/>
      <polygon points="682,0 706,0 495,240 722,672 698,672 470,240" fill="var(--red)"/>
    </svg>
    <div class="event-tag">CAR WASH</div>
    <div class="school-name">
      <span class="school-name__mark"></span>
      <div class="school-name__text">STONEMERE HEIGHTS<br>COLLEGE</div>
    </div>
    <div class="event-date">Sunday June 12</div>
    <div class="event-cause">HELP SUPPORT<br>Year 9<br>Singapore Trip!!!</div>
  </section>

  <section class="slide slide--holidays">
    <svg class="shapes" width="1008" height="640" viewBox="0 0 1008 640">
      <defs>
        <linearGradient id="studentsScene" x1="0" y1="0" x2="1" y2="0">
          <stop offset="0" stop-color="#d9c7b8"/>
          <stop offset=".3" stop-color="#6f90c2"/>
          <stop offset=".6" stop-color="#c9474f"/>
          <stop offset=".85" stop-color="#8c95a6"/>
          <stop offset="1" stop-color="#ffffff"/>
        </linearGradient>
        <linearGradient id="bandGlow" x1="0" y1="0" x2="1" y2="1">
          <stop offset=".7" stop-color="var(--blue)"/>
          <stop offset="1" stop-color="#4a78b0"/>
        </linearGradient>
      </defs>
      <rect x="0" y="44" width="640" height="280" fill="url(#studentsScene)" role="img" aria-label="Photo of a group of five happy students sitting together"/>
      <path d="M0,300 Q350,270 1008,352 L1008,640 L0,640 Z" fill="var(--red)"/>
      <path d="M0,308 Q350,280 1008,360 L1008,640 L0,640 Z" fill="url(#bandGlow)"/>
    </svg>
    <div class="school-name">
      <span class="school-name__mark"></span>
      <div class="school-name__text">STONEMERE HEIGHTS<br>COLLEGE</div>
    </div>
    <div class="holiday-copy holiday-copy--title">School Holidays Start<br>Friday September 8<sup>th</sup></div>
    <div class="holiday-copy holiday-copy--sub">School re-opens Monday September 25<sup>th</sup></div>
  </section>

</div>
</div>
</body>
</html>
```